Wordpress Design Project for Employee Communications Site

We need a Wordpress design for a company that strategizes on and produces materials for employee communications. Improving employee communications at all levels of an organization can help improve overall company performance and results. The site needs to look very clean and professional; we're not afraid of white space. We like the functionality that Wordpress provides; however, we only want one "true" blog page; the other pages should give the impression of a more "static" web site - particularly the home page. I have a logo that I can provide.

I have added these comments to the discussion page:
Great question - thank you for asking it. I’ve done more research

I like the very clean and monochromatic looks to many of these. I don’t have to have monochromatic, but I do like minimal colors. Simple, clean, organized. The home page should “fit” almost entirely without scrolling. I do like fat footers that you can scroll down to. I don’t want a colored background, but any that I’ve chosen with colored backgrounds could be switched to a white background.

http://www.moravelkinst.com/
http://pondrix.com/
http://v1.belmarquist.com/
http://howtheotter.com/
http://stayingnimble.com/
http://www.interiors.pelmun.co.uk/
http://brixalumnihub.com/

These last two are more corporate sites. The first one is from a well-respected consultant in my area who does a lot of what I do. And I think Harwick does a nice job with their site. So, I want to marry the look I like with getting the content job done.

http://www.messagefuelworks.com/
http://www.harwick.com/view/en_US/us/index.htm

Target Market(s)

Target market is mid- to large-sized companies. More than 500 employees.

Industry/Entity Type

Communications

Requirements
Must have
• Need an impactful home page. There should be a "blog" page; contact us; services; about. For starters, at least. I want fonts to be very readable - that is, either quite dark gray or black.
Nice to have
• I am loathe to include a picture of myself, but I do want some images that say, "professional" and "expert" in communications.
Should not have
• I don't want a hits counter :) (I know no one would do that!).

```html
<!DOCTYPE html>
<html lang="en">
<head>
<meta charset="utf-8">
<title>Corvane Communications Group</title>
<link href="https://fonts.googleapis.com/css2?family=Open+Sans:wght@400;700&family=Oswald:wght@400&family=Noto+Sans:wght@400;700&display=swap" rel="stylesheet">
<style>
:root{
  --lime:#c2d93a;
  --sky:#6ec3e8;
  --sky-pale:#b2dff1;
  --page:#fafbef;
  --white:#ffffff;
  --ink:#333333;
  --text:#3a3a3a;
  --nav:#8c8c8c;
  --rule:#e4e4e4;
  --dot:#9a9a9a;
}
*{margin:0;padding:0;box-sizing:border-box}
html,body{width:1200px;height:1052px;overflow:hidden}
body{position:relative;background:var(--page);font-family:"Noto Sans",sans-serif;color:var(--text)}
.top-bar{position:absolute;left:0;top:0;width:1200px;height:10px;background:var(--lime)}
.sheet{position:absolute;left:189px;top:10px;width:840px;height:974px;background:var(--white);box-shadow:0 0 12px rgba(0,0,0,.06)}
.brand{position:absolute;left:217px;top:42px;display:flex;align-items:center;gap:14px}
.brand-dot{width:58px;height:58px;border-radius:50%;background:var(--sky)}
.brand-name{font-family:"Open Sans",sans-serif;font-weight:400;font-size:52px;color:var(--lime);letter-spacing:1px}
.main-nav{position:absolute;left:603px;top:100px;display:flex;font-family:"Open Sans",sans-serif;font-weight:700;font-size:15px}
.main-nav a{display:block;height:48px;padding:10px 0 0;color:var(--nav);text-decoration:none;margin-right:26px}
.main-nav a.current{background:var(--sky);color:var(--white);padding:10px 9px 0;margin-right:16px}
.main-nav a:last-child{margin-right:0}
.hero{position:absolute;left:210px;top:150px;width:801px;height:391px;border:1px solid #cfd6da;background:linear-gradient(100deg,#e8e4df 0%,#d9d2ca 35%,#c9b8a8 55%,#f2f1ee 75%,#b9c4cc 100%)}
.hero-caption{position:absolute;left:210px;top:414px;width:306px;height:110px;background:var(--sky);border-radius:0 10px 10px 0;padding:12px 0 0 19px;color:var(--ink)}
.hero-caption h1{font-family:"Oswald",sans-serif;font-weight:400;font-size:28px;line-height:34px;transform:scaleX(.9);transform-origin:left}
.hero-caption p{font-family:"Open Sans",sans-serif;font-size:15px;line-height:20px;color:#3c4a52;margin-top:3px}
.slide-arrow{position:absolute;top:306px}
.slide-arrow.prev{left:130px}
.slide-arrow.next{left:1040px}
.slide-dots{position:absolute;left:942px;top:553px;display:flex;gap:7px}
.slide-dots span{width:12px;height:12px;border-radius:50%;background:var(--dot)}
.slide-dots span.active{background:var(--sky)}
.block{position:absolute;width:228px}
.block h2{font-family:"Oswald",sans-serif;font-weight:400;font-size:21px;color:var(--ink);transform:scaleX(.88);transform-origin:left;white-space:nowrap;line-height:26px}
.block p{font-size:12px;line-height:15.6px;letter-spacing:.45px;text-align:justify;margin-top:8px;color:var(--text)}
.read-more{display:flex;align-items:center;gap:6px;margin-top:11px;font-size:12px;font-weight:700;color:var(--ink);text-decoration:none}
.read-more i{width:20px;height:12px;border-radius:6px;background:var(--sky);display:block}
.credit{text-align:right;font-size:12px;font-weight:700;line-height:14.5px;margin-top:6px;color:var(--ink)}
.divider{position:absolute;width:1px;background:var(--rule)}
.site-footer{position:absolute;left:0;top:984px;width:1200px;height:68px;background:var(--sky-pale)}
.footer-brand{position:absolute;left:210px;top:1003px;display:flex;align-items:center;gap:6px}
.footer-brand span{width:20px;height:20px;border-radius:50%;background:#8f9aa0}
.footer-brand b{font-family:"Open Sans",sans-serif;font-weight:400;font-size:22px;color:#8f9aa0}
.footer-nav{position:absolute;left:424px;top:1003px;font-family:"Open Sans",sans-serif;font-size:13px;color:#222;word-spacing:2px}
.footer-nav a{color:#222;text-decoration:none}
.footer-nav em{font-style:normal;margin:0 14px}
.copyright{position:absolute;left:441px;top:1033px;font-family:"Open Sans",sans-serif;font-size:10px;color:#222}
.social{position:absolute;left:942px;top:998px;display:flex;gap:-6px}
.social span{width:34px;height:34px;border-radius:50%}
.social .one{background:var(--sky)}
.social .two{background:var(--lime);margin-left:-4px}
</style>
</head>
<body>
<div class="top-bar"></div>
<div class="sheet"></div>

<div class="brand" aria-label="Corvane">
  <span class="brand-dot"></span>
  <span class="brand-name">Corvane</span>
</div>

<nav class="main-nav">
  <a href="#" class="current">HOME</a>
  <a href="#">ABOUT</a>
  <a href="#">SERVICES</a>
  <a href="#">BLOG</a>
  <a href="#">CONTACT US</a>
</nav>

<div class="hero" role="img" aria-label="Photo of a smiling businesswoman in a dark suit with colleagues meeting at a table behind her"></div>
<div class="hero-caption">
  <h1>Effective Communication</h1>
  <p>Effective communication in the work-<br>place is the backbone of any business.</p>
</div>

<svg class="slide-arrow prev" width="36" height="40" viewBox="0 0 36 40"><polygon points="36,0 22,0 0,20 22,40 36,40 14,20" fill="var(--lime)"/></svg>
<svg class="slide-arrow next" width="36" height="40" viewBox="0 0 36 40"><polygon points="0,0 14,0 36,20 14,40 0,40 22,20" fill="var(--lime)"/></svg>

<div class="slide-dots"><span class="active"></span><span></span><span></span><span></span></div>

<section class="block" style="left:209px;top:605px">
  <h2>External Communication</h2>
  <p>Effective communication in the work-place is the backbone of any business. Without it, you could miss out on important opportunities, waste time and cause your employees and custom-ers to become frustrated.</p>
  <a class="read-more" href="#"><i></i>Read More</a>
</section>
<section class="block" style="left:488px;top:605px">
  <h2>Business Growth</h2>
  <p>Effective communication in the work-place is the backbone of any business. Without it, you could miss out on important opportunities, waste time and cause your employees and custom-ers to become frustrated.</p>
  <a class="read-more" href="#"><i></i>Read More</a>
</section>
<section class="block" style="left:764px;top:605px">
  <h2>Internal Communication</h2>
  <p>Effective communication in the work-place is the backbone of any business. Without it, you could miss out on important opportunities, waste time and cause your employees and custom-ers to become frustrated.</p>
  <a class="read-more" href="#"><i></i>Read More</a>
</section>

<section class="block" style="left:209px;top:801px">
  <h2>What Customers are Saying...</h2>
  <p>Corvane is a great benchmarking tool."The Corvane channels offer a very effective way to communicate with geographi-cally distributed stores and in a retail environment."</p>
  <div class="credit" style="margin-right:6px">Marissa Delvane<br>Internal Communications<br>Manager</div>
</section>
<section class="block" style="left:488px;top:801px">
  <h2>Internal Social Media</h2>
  <p>Corvane is a great benchmarking tool."The Corvane channels offer a very effective way to communicate with geographi-cally distributed stores and in a retail environment."</p>
  <div class="credit">Specifically for employee<br>communication</div>
</section>
<section class="block" style="left:765px;top:801px">
  <h2>Business Growth</h2>
  <p>Corvane is a great benchmarking tool."The Corvane channels offer a very effective way to communicate with geographi-cally distributed stores and in a retail environment."</p>
  <div class="credit">Specifically for employee<br>communication</div>
</section>

<div class="divider" style="left:461px;top:628px;height:104px"></div>
<div class="divider" style="left:737px;top:628px;height:104px"></div>
<div class="divider" style="left:461px;top:828px;height:104px"></div>
<div class="divider" style="left:740px;top:828px;height:104px"></div>

<footer class="site-footer"></footer>
<div class="footer-brand"><span></span><b>Corvane</b></div>
<div class="footer-nav"><a href="#">Home</a><em>|</em><a href="#">About</a><em>|</em><a href="#">Services</a><em>|</em><a href="#">Blog</a><em>|</em><a href="#">Contact Us</a></div>
<div class="copyright">All rights reserved. © Corvane Communications Group 2008</div>
<div class="social"><span class="one"></span><span class="two"></span></div>
</body>
</html>
```